integrative health clinic-Medical massage, acupuncture, chiropractic

we like our logo, but are open to new ideas. We need a new card design. We have added chiropractic and acupuncture that we have put under the name of the business. We are an integrative medical clinic

Target Market(s)

General public, athletes

Contact Information for Business Card

Phone 5055583927
Fax 5055583926
Hours Monday-Friday 9-6
Saturday 10-6
The 20% can be smaller on the back

Colors
3176b5
0355a3

Requirements
Must have
• Logo but am open to ideas
Nice to have
• We are an integrated medical clinic but also want to be personable. We want the card fun and inviting

```html
<!DOCTYPE html>
<html lang="en">
<head>
<meta charset="utf-8">
<title>True Balance Wellness – Business Card</title>
<link rel="stylesheet" href="https://fonts.googleapis.com/css2?family=Carlito:ital,wght@0,400;0,700;1,400;1,700&display=swap">
<style>
  :root {
    --brand-blue: #0355a3;
    --brand-light: #3176b5;
    --navy: #0f3a78;
    --ink: #111111;
    --text-grey: #333333;
    --page: #ffffff;
    --card: #ffffff;
  }
  * { box-sizing: border-box; margin: 0; padding: 0; }
  html, body {
    width: 1049px; height: 1200px; overflow: hidden;
    background: var(--page);
    font-family: "Carlito", "Calibri", sans-serif;
  }
  .canvas { position: relative; width: 1049px; height: 1200px; }

  .card {
    position: absolute; left: 85px; width: 884px; height: 491px;
    background: var(--card);
    box-shadow: 0 2px 10px rgba(0,0,0,0.12);
    overflow: hidden;
  }
  .card--front { top: 80px; }
  .card--back { top: 640px; }

  /* Front */
  .brand {
    position: absolute; left: 225px; top: 82px;
    display: flex; align-items: center; gap: 28px;
  }
  .brand__dot {
    width: 92px; height: 92px; border-radius: 50%;
    background: var(--brand-blue);
  }
  .brand__name {
    font-weight: 700; font-size: 52px; line-height: 44px;
    color: var(--ink); letter-spacing: 1px;
  }
  .tagline {
    position: absolute; left: 0; right: 0; top: 223px;
    text-align: center; font-style: italic; font-weight: 700;
    font-size: 31px; color: var(--ink); letter-spacing: 1px;
  }
  .contact {
    position: absolute; left: 0; right: 0; top: 290px;
    text-align: center; font-size: 27px; line-height: 39px;
    color: var(--text-grey);
  }
  .contact__row span + span { margin-left: 48px; }
  .band {
    position: absolute; left: 0; right: 0; bottom: 0; height: 58px;
    background: var(--brand-blue);
    display: flex; align-items: center; justify-content: center;
    color: #fff; font-style: italic; font-size: 31px; letter-spacing: 2px;
    word-spacing: 8px;
  }

  /* Back */
  .back__photo {
    position: absolute; inset: 0;
    background: linear-gradient(115deg, #f2ece8 0%, #ead6c6 35%, #f3e7dd 55%, #d9d6da 80%, #cfcdd2 100%);
  }
  .back__frame {
    position: absolute; left: 39px; top: 33px; width: 806px; height: 422px;
    border: 3px solid var(--brand-blue); border-radius: 44px;
  }
  .booking {
    position: absolute; left: 0; right: 0; top: 82px;
    text-align: center; color: var(--navy); font-weight: 700;
    font-size: 30px; line-height: 38px;
  }
  .hours-mark {
    position: absolute; left: 185px; top: 187px;
    width: 106px; height: 106px; border-radius: 50%;
    background: var(--brand-blue);
  }
  .hours {
    position: absolute; left: 323px; top: 183px;
    color: var(--navy); font-weight: 700; font-size: 35px; line-height: 43px;
  }
  .services {
    position: absolute; left: 0; right: 0; top: 336px;
    text-align: center; color: var(--navy); font-style: italic; font-weight: 700;
  }
  .services__intro { font-size: 23px; line-height: 30px; }
  .services__list { font-size: 28px; line-height: 35px; }
</style>
</head>
<body>
<main class="canvas">

  <section class="card card--front" aria-label="Card front">
    <div class="brand">
      <div class="brand__dot" aria-hidden="true"></div>
      <div class="brand__name">TRUE<br>BALANCE<br>WELLNESS</div>
    </div>
    <p class="tagline">Sports Theraphy &amp; Wellness Centre</p>
    <div class="contact">
      <p class="contact__row"><span>Phone (505) 558-3927</span><span>Fax (505) 558-3926</span></p>
      <p>1487 Cerrillos Way, B4, Santa Fe, NM 87507</p>
      <p>info@truebalancewellnessnm.com</p>
    </div>
    <div class="band">EXPERIENCE THE DIFFERENCE</div>
  </section>

  <section class="card card--back" aria-label="Card back">
    <div class="back__photo" role="img" aria-label="Soft faded photo of a therapist massaging a client's leg"></div>
    <div class="back__frame"></div>
    <div class="booking">
      <p>Book online @ truebalancewellnessnm.com</p>
      <p>20% Off first visit</p>
    </div>
    <div class="hours-mark" aria-hidden="true"></div>
    <div class="hours">
      <p>Hours:</p>
      <p>Monday-Friday 9am-6pm</p>
      <p>Saturday 10am-6pm</p>
    </div>
    <div class="services">
      <p class="services__intro">Specialising in</p>
      <p class="services__list">Medical &amp; Sports Massage, Manual Therapies<br>Acupuncture, Chiropractic, Skin Therapy</p>
    </div>
  </section>

</main>
</body>
</html>
```